Custom hot rod builder needs a website for launch of new business where he will build luxury garages

We need a website that gives a WOW first impression for "Summit Carhouses". This is a new business so photos are renderings but we need it to really attract a particular audience. Our initial business is custom hot rods so now we are building garages for them. These will be like luxury "homes" for cars! I will attach our new logo. Website needs to feel powerful and prestigious.

Target Market(s)

middle aged men, car enthusiasts

Industry/Entity Type

automotive, construction

Coding

Coded - Design and coding required

Number of Pages Required

2 page

Font styles to use
Serif

Colors
0054AA
0677BA
7BADD7
CADEEF
E8F1F8

Requirements
Must have
• a WOW factor. luxury. contact form.
Nice to have
• ?

```html
<!DOCTYPE html>
<html lang="en">
<head>
<meta charset="utf-8">
<title>Summit Carhouses</title>
<link href="https://fonts.googleapis.com/css2?family=Orbitron:wght@700;800;900&family=Lora:wght@400;500;600&display=swap" rel="stylesheet">
<style>
:root{
  --blue:#2ea3dd;
  --blue-deep:#1b8ccc;
  --ink:#1c1c1c;
  --text:#3a3a3a;
  --white:#ffffff;
  --footer:#121212;
  --field-text:#9a9a9a;
  --photo-warm:#d9a03a;
  --photo-deep:#b8432f;
}
*{margin:0;padding:0;box-sizing:border-box}
html,body{width:1200px;height:3353px;overflow:hidden}
body{position:relative;font-family:'Lora',serif;color:var(--text);background:var(--white)}
.abs{position:absolute}
.display{font-family:'Orbitron',sans-serif;font-weight:800;text-transform:uppercase;letter-spacing:1px}

/* hero */
.hero{left:0;top:0;width:1200px;height:599px;background:linear-gradient(180deg,#4a5157 0%,#3a4146 45%,#6b6f70 72%,#8a8c8b 100%)}
.nav{left:112px;top:53px;width:976px;height:89px;background:var(--white);border-radius:4px;display:flex;align-items:center;padding:0 28px 0 18px}
.brand{display:flex;align-items:center;gap:10px;font-family:'Lora',serif;font-weight:600;font-size:17px;color:var(--blue);width:220px;white-space:nowrap}
.brand-dot{width:44px;height:44px;border-radius:50%;background:var(--blue);flex:none}
.nav-links{display:flex;gap:36px;list-style:none;font-size:15px;color:#222;margin-left:8px;white-space:nowrap}
.nav-links .active{color:var(--blue)}
.btn{display:flex;align-items:center;justify-content:space-between;border-radius:24px;font-family:'Orbitron',sans-serif;font-weight:800;text-transform:uppercase;letter-spacing:1px;font-size:15px;padding:0 6px 0 20px;white-space:nowrap}
.btn .arrow{width:34px;height:34px;border-radius:50%;display:flex;align-items:center;justify-content:center}
.btn-solid{background:var(--blue);color:var(--white)}
.btn-solid .arrow{background:var(--white)}
.btn-light{background:var(--white);color:var(--blue);border:2px solid var(--white)}
.btn-light .arrow{background:var(--blue)}
.login{margin-left:auto;width:142px;height:43px}
.hero-sub{left:0;width:1200px;top:246px;text-align:center;color:var(--white);font-size:39px}
.hero-title{left:0;width:1200px;top:298px;text-align:center;color:var(--white);font-size:58px;font-weight:900}
.get-started{left:491px;top:385px;width:216px;height:42px}
.dots{left:579px;top:538px;display:flex;gap:6px}
.dots span{width:9px;height:9px;border-radius:50%;background:var(--white)}
.dots span.on{background:var(--blue)}

/* headings */
.section-title{left:0;width:1200px;text-align:center;font-size:31px;color:var(--ink)}
.rule{left:568px;width:64px;height:3px;background:var(--blue)}

/* features */
.feature{width:360px;text-align:center}
.feature-ring{position:relative;width:170px;height:170px;margin:0 auto}
.feature h3{font-family:'Orbitron',sans-serif;font-weight:800;font-size:18px;letter-spacing:1px;color:var(--ink);margin-top:44px}
.feature p{font-size:15px;line-height:26px;margin-top:22px;color:#444}
.feature .more{display:block;margin-top:18px;font-family:'Orbitron',sans-serif;font-weight:800;font-size:11px;letter-spacing:1px;color:var(--blue)}

/* about */
.about{left:0;top:1229px;width:1200px;height:558px;background:var(--blue)}
.about-photo{left:20px;top:122px;width:516px;height:348px;border-radius:6px;background:linear-gradient(135deg,var(--photo-warm) 0%,var(--photo-deep) 100%)}
.about-title{left:601px;top:97px;font-size:34px;line-height:43px;color:var(--white)}
.about-copy{left:601px;top:197px;width:487px;font-size:15px;line-height:26px;color:var(--white);text-align:justify}
.about-btn{left:601px;top:408px;width:216px;height:45px}

/* services */
.card{top:1974px;width:309px;height:379px;box-shadow:0 2px 6px rgba(0,0,0,.25)}
.card-workshop{left:113px;background:linear-gradient(180deg,#8d9296,#5f6468 55%,#3c3f42)}
.card-feature{left:446px;background:linear-gradient(180deg,#43aee0,#5bb9e4);color:var(--white);text-align:center}
.card-night{left:780px;background:linear-gradient(180deg,#6f7173,#4c4d4e 60%,#a88658 80%,#2e2e2e)}
.card-feature h4{font-size:22px;margin-top:73px}
.card-feature p{font-size:15px;line-height:26px;margin:29px 18px 0}
.card-feature .btn{position:absolute;left:46px;top:256px;width:218px;height:43px}

/* contact */
.contact{left:0;top:2439px;width:1200px;height:553px;background:linear-gradient(180deg,#2b9bd6,#1f8fcf)}
.field{background:var(--white);border:none;border-radius:6px;font-family:'Lora',serif;font-size:15px;color:var(--field-text);padding:0 24px;display:flex;align-items:center}
.field.area{align-items:flex-start;padding-top:18px}
.submit{left:514px;top:445px;width:172px;height:43px}

/* footer */
.footer{left:0;top:2992px;width:1200px;height:361px;background:var(--footer);color:var(--white)}
.footer-brand{left:107px;top:96px;width:220px;text-align:center}
.footer-brand .mark{width:98px;height:98px;border-radius:50%;background:var(--blue);margin:0 auto 18px}
.footer-brand span{font-family:'Lora',serif;font-weight:600;font-size:20px;color:var(--blue);white-space:nowrap}
.footer h5{font-family:'Lora',serif;font-weight:600;font-size:19px}
.footer ul{list-style:none;font-size:15px;line-height:26px}
.contact-row{display:flex;gap:12px;font-size:15px;line-height:26px}
.contact-row svg{flex:none;margin-top:6px}
.social{display:flex;gap:16px}
.social span{width:42px;height:42px;border-radius:50%;background:var(--blue)}
.copyright{left:0;top:306px;width:1200px;text-align:center;font-size:15px}
</style>
</head>
<body>

<section class="abs hero" role="img" aria-label="Rendering of a modern luxury garage house at dusk with classic cars behind glass">
  <nav class="abs nav">
    <div class="brand"><span class="brand-dot"></span>Summit Carhouses</div>
    <ul class="nav-links">
      <li class="active">HOME</li><li>WHY CHOOSE</li><li>SERVICES</li><li>ABOUT</li><li>COTACT US</li>
    </ul>
    <div class="btn btn-solid login">Log in<span class="arrow"><svg width="18" height="10" viewBox="0 0 18 10"><path d="M0 5h16M12 1l4 4-4 4" stroke="#2ea3dd" stroke-width="1.6" fill="none"/></svg></span></div>
  </nav>
  <div class="abs display hero-sub">Welcome to</div>
  <h1 class="abs display hero-title">Summit Carhouses</h1>
  <div class="abs btn btn-solid get-started">Get started<span class="arrow"><svg width="18" height="10" viewBox="0 0 18 10"><path d="M0 5h16M12 1l4 4-4 4" stroke="#2ea3dd" stroke-width="1.6" fill="none"/></svg></span></div>
  <div class="abs dots"><span></span><span class="on"></span><span></span></div>
</section>

<h2 class="abs display section-title" style="top:677px">Why choose us</h2>
<div class="abs rule" style="top:723px"></div>

<div class="abs feature" style="left:71px;top:790px">
  <div class="feature-ring">
    <svg width="170" height="170" viewBox="0 0 170 170">
      <path d="M85 4 A81 81 0 1 0 166 85" stroke="#2ea3dd" stroke-width="10" fill="none"/>
      <circle cx="90" cy="81" r="76" fill="#fff" style="filter:drop-shadow(0 2px 4px rgba(0,0,0,.15))"/>
      <circle cx="90" cy="81" r="28" stroke="#2ea3dd" stroke-width="3" fill="none" stroke-dasharray="10 5"/>
      <circle cx="90" cy="81" r="18" stroke="#2ea3dd" stroke-width="3" fill="none"/>
      <path d="M80 81l7 7 13-13" stroke="#2ea3dd" stroke-width="3" fill="none"/>
    </svg>
  </div>
  <h3>UNDER YOUR CONTROL</h3>
  <p>Lorem ipsum dolor sit amet,<br>consectetur adipiscing elit, sed do<br>eiusmod tempor incididunt</p>
  <span class="more">LEARN MORE</span>
</div>
<div class="abs feature" style="left:428px;top:790px">
  <div class="feature-ring">
    <svg width="170" height="170" viewBox="0 0 170 170">
      <path d="M85 4 A81 81 0 1 0 166 85" stroke="#2ea3dd" stroke-width="10" fill="none"/>
      <circle cx="90" cy="81" r="76" fill="#fff" style="filter:drop-shadow(0 2px 4px rgba(0,0,0,.15))"/>
      <path d="M53 62 L90 43 L127 62 V118 H53 Z" stroke="#2ea3dd" stroke-width="3" fill="none"/>
      <rect x="67" y="72" width="46" height="40" stroke="#2ea3dd" stroke-width="3" fill="none"/>
      <path d="M72 100h36M76 92l5-10h18l5 10" stroke="#2ea3dd" stroke-width="3" fill="none"/>
      <circle cx="90" cy="55" r="5" stroke="#2ea3dd" stroke-width="2" fill="none"/>
    </svg>
  </div>
  <h3>COMMON GROUND</h3>
  <p>Lorem ipsum dolor sit amet,<br>consectetur adipiscing elit, sed do<br>eiusmod tempor incididunt</p>
  <span class="more">LEARN MORE</span>
</div>
<div class="abs feature" style="left:785px;top:790px">
  <div class="feature-ring">
    <svg width="170" height="170" viewBox="0 0 170 170">
      <path d="M85 4 A81 81 0 1 0 166 85" stroke="#2ea3dd" stroke-width="10" fill="none"/>
      <circle cx="90" cy="81" r="76" fill="#fff" style="filter:drop-shadow(0 2px 4px rgba(0,0,0,.15))"/>
      <path d="M90 48 L118 58 V80 C118 98 105 110 90 116 C75 110 62 98 62 80 V58 Z" stroke="#2ea3dd" stroke-width="3" fill="none"/>
      <path d="M77 80l9 9 18-18" stroke="#2ea3dd" stroke-width="3" fill="none"/>
    </svg>
  </div>
  <h3>SAFE &amp; SECURE</h3>
  <p>Lorem ipsum dolor sit amet,<br>consectetur adipiscing elit, sed do<br>eiusmod tempor incididunt</p>
  <span class="more">LEARN MORE</span>
</div>

<section class="abs about">
  <div class="abs about-photo" role="img" aria-label="Photo of a red and yellow flamed custom hot rod with open hood"></div>
  <h2 class="abs display about-title">About Summit<br>Carhouses</h2>
  <p class="abs about-copy">Lorem ipsum dolor sit amet, consectetur adipiscing elit, sed do eiusmod tempor incididunt ut labore et dolore magna aliqua. Ut enim ad minim veniam, quis nostrud exercitation ullamco laboris nisi ut aliquip ex ea commodo consequat. Duis aute irure dolor in reprehenderit in voluptate velit esse cillum dolore eu fugiat nulla pariatur. Excepteur sint occaecat cupidatat non proident, sunt in culpa qui officia deserunt mollit anim id est laborum.</p>
  <div class="abs btn btn-light about-btn">Learn more<span class="arrow"><svg width="18" height="10" viewBox="0 0 18 10"><path d="M0 5h16M12 1l4 4-4 4" stroke="#fff" stroke-width="1.6" fill="none"/></svg></span></div>
</section>

<h2 class="abs display section-title" style="top:1866px">Our services</h2>
<div class="abs rule" style="top:1912px"></div>
<div class="abs card card-workshop" role="img" aria-label="Photo of a bright workshop with car lifts"></div>
<div class="abs card card-feature">
  <h4 class="display">Lorem ipsum</h4>
  <p>Lorem ipsum dolor sit amet, consectetur adipiscing elit, sed do eiusmod tempor incididunt ut labore et dolore magna aliqua.</p>
  <div class="btn btn-light">Learn more<span class="arrow"><svg width="18" height="10" viewBox="0 0 18 10"><path d="M0 5h16M12 1l4 4-4 4" stroke="#fff" stroke-width="1.6" fill="none"/></svg></span></div>
</div>
<div class="abs card card-night" role="img" aria-label="Rendering of a concrete garage at night with a sports car charging"></div>

<section class="abs contact">
  <h2 class="abs display section-title" style="top:68px;color:#fff">Our services</h2>
  <div class="abs rule" style="top:114px;background:#fff"></div>
  <div class="abs field" style="left:262px;top:161px;width:333px;height:58px">First name*</div>
  <div class="abs field" style="left:604px;top:161px;width:333px;height:58px">Last name*</div>
  <div class="abs field" style="left:262px;top:234px;width:333px;height:58px">Phone*</div>
  <div class="abs field" style="left:604px;top:234px;width:333px;height:58px">Email*</div>
  <div class="abs field area" style="left:262px;top:307px;width:675px;height:117px">Message</div>
  <div class="abs btn btn-light submit">Submit<span class="arrow"><svg width="18" height="10" viewBox="0 0 18 10"><path d="M0 5h16M12 1l4 4-4 4" stroke="#fff" stroke-width="1.6" fill="none"/></svg></span></div>
</section>

<footer class="abs footer">
  <div class="abs footer-brand"><div class="mark"></div><span>Summit Carhouses</span></div>
  <h5 class="abs" style="left:445px;top:79px">Quick Links</h5>
  <ul class="abs" style="left:446px;top:123px"><li>Home</li><li>Why Choose</li><li>Services</li><li>About</li><li>Cotact Us</li></ul>
  <h5 class="abs" style="left:604px;top:79px">Contact Us</h5>
  <div class="abs" style="left:604px;top:122px">
    <div class="contact-row"><svg width="14" height="16" viewBox="0 0 14 16"><path d="M7 0C3 0 1 3 1 6c0 4 6 10 6 10s6-6 6-10c0-3-2-6-6-6z" fill="#fff"/><circle cx="7" cy="6" r="2" fill="#121212"/></svg><span>Lorem ipsum dolor sit amet,<br>consectetur adipiscing</span></div>
    <div class="contact-row" style="margin-top:14px"><svg width="14" height="14" viewBox="0 0 14 14"><path d="M3 0l3 3-2 2c1 2 3 4 5 5l2-2 3 3-2 3C6 14 0 8 0 3z" fill="#fff"/></svg><span>+1 (555) 204 7781</span></div>
    <div class="contact-row" style="margin-top:13px"><svg width="14" height="11" viewBox="0 0 14 11"><rect width="14" height="11" fill="#fff"/><path d="M0 0l7 6 7-6" stroke="#121212" fill="none"/></svg><span>info@summitcarhouses.com</span></div>
  </div>
  <h5 class="abs" style="left:872px;top:79px">Follow us</h5>
  <div class="abs social" style="left:873px;top:130px" aria-label="Social media links"><span></span><span></span><span></span><span></span></div>
  <p class="abs copyright">©Copyrights 2022 Summit Carhouses &nbsp; | &nbsp; All Rights Reserved</p>
</footer>

</body>
</html>
```